Bed and Breakfast WebSite Design

We need a webdesign for a bed and breakfast in Germany. This house is located at the scenic river Mosel in Germany, a very small town called Piesport. It's a region known for its wines. A lot of nature, bicycle routes, hiking, boat tours...

The house itself is a former monastery and because of that a listed, historic buildung.
The house is entirely renewed and has a very modern, individual interieur with "boutique hotel" style rooms. Every room is different. Its family owned and operated.

The website should find a bridge between historic charme and modern individual friendlyness. Very straight, not fancy. The website should express familiy friendlyness, modern comfort and emphasize that its place to RELAX.

In the attachment you'll find a lot of photos of house and surrounding. Theres a separate zip with lumetra stockphotos of that particular location/town (not purchased yet).

Number of Pages Required

1 page

Requirements
Must have
• Should be "easily" made responsive.

```html
<!DOCTYPE html>
<html lang="en">
<head>
<meta charset="utf-8">
<title>Haus Weinberg – Bed &amp; Breakfast</title>
<link href="https://fonts.googleapis.com/css2?family=Poppins:wght@400;500;600;700&family=Open+Sans:wght@400;600;700&display=swap" rel="stylesheet">
<style>
:root{
  --green:#6a9a2c;
  --green-dark:#557f1f;
  --green-pale:#f1f7e6;
  --ink:#2b2b2b;
  --muted:#6e6e6e;
  --white:#ffffff;
  --dark:#1e1e1e;
  --darker:#151515;
  --line:#e3e3e3;
  --star:#f2a516;
}
*{box-sizing:border-box;margin:0;padding:0}
html,body{width:1200px;height:4092px;overflow:hidden}
body{font-family:"Open Sans",Arial,sans-serif;color:var(--ink);background:var(--white);font-size:14px;line-height:1.6}
.wrap{width:860px;margin:0 auto;position:relative}
h1,h2,h3,h4,.brand{font-family:"Poppins",Arial,sans-serif}

/* top bar */
.topbar{height:32px;background:var(--green);color:var(--white);font-size:12px}
.topbar .wrap{display:flex;justify-content:space-between;align-items:center;height:32px}
.socials{display:flex;gap:6px}
.socials span{width:20px;height:20px;border:1.5px solid var(--white);border-radius:50%;display:block}
.top-contact{display:flex;gap:22px;align-items:center}
.top-contact div{display:flex;gap:6px;align-items:center}

/* nav */
.nav{height:80px;background:var(--white)}
.nav .wrap{display:flex;justify-content:space-between;align-items:center;height:80px}
.brand{font-size:24px;font-weight:600;color:var(--green)}
.menu{display:flex;gap:26px;align-items:center;font-family:"Poppins",sans-serif;font-size:13px;font-weight:500;text-transform:uppercase}
.menu a{color:var(--ink);text-decoration:none}
.menu a.active{color:var(--green)}
.btn{display:inline-block;background:var(--green);color:var(--white);font-family:"Poppins",sans-serif;font-weight:600;font-size:13px;border-radius:22px;padding:10px 22px;text-decoration:none}

/* hero */
.hero{height:668px;position:relative;background:linear-gradient(180deg,#3f5a2c 0%,#5d7347 35%,#7c8a6a 60%,#6f7362 100%);text-align:center;color:var(--white)}
.hero-shade{position:absolute;inset:0;background:rgba(0,0,0,.18)}
.hero-copy{position:relative;padding-top:300px}
.hero h1{font-size:54px;font-weight:700;letter-spacing:1px;text-transform:uppercase;line-height:1.1}
.hero p{font-family:"Poppins",sans-serif;font-weight:600;font-size:16px;text-transform:uppercase;margin:12px 0 30px}
.booking{position:absolute;left:180px;top:608px;width:840px;height:108px;background:var(--white);border-radius:4px;box-shadow:0 8px 24px rgba(0,0,0,.15);display:flex;align-items:center;gap:18px;padding:0 22px;color:var(--ink);text-align:left}
.field{flex:1}
.field label{display:block;font-size:12px;font-weight:600;margin-bottom:6px}
.field .box{height:38px;border:1px solid var(--line);border-radius:3px;font-size:12px;color:var(--muted);display:flex;align-items:center;justify-content:space-between;padding:0 10px}
.booking .btn{border-radius:4px;padding:12px 18px;margin-top:22px}

/* welcome */
.welcome{height:560px;padding-top:108px}
.welcome .wrap{display:flex;justify-content:space-between;width:860px}
.welcome-text{width:310px;padding-top:60px}
.welcome-text h4{font-size:16px;font-weight:500;text-transform:uppercase}
.welcome-text h2{font-size:30px;font-weight:600;color:var(--green);line-height:1.2;margin-bottom:22px}
.welcome-text p{font-size:13px;color:var(--muted);margin-bottom:18px}
.welcome-photos{width:460px;display:grid;grid-template-columns:220px 220px;grid-template-rows:216px 216px;gap:12px 20px}
.photo{border-radius:2px}
.ph-night{background:linear-gradient(160deg,#162033,#35404a 60%,#1f2a30)}
.ph-valley{background:linear-gradient(180deg,#6e8aa8,#587c45 55%,#3b5d2c);grid-row:span 2;height:100%}
.ph-candle{background:linear-gradient(160deg,#2a1408,#7a3a16 50%,#3b1d0c)}

/* rooms */
.rooms{height:850px;background:var(--green-pale);padding-top:120px;text-align:center}
.section-title{font-size:36px;font-weight:600;color:var(--ink)}
.section-title span{color:var(--green)}
.section-sub{font-size:12px;color:var(--muted);width:420px;margin:4px auto 40px;line-height:1.5}
.room-grid{display:grid;grid-template-columns:repeat(3,280px);gap:12px 10px;justify-content:center}
.room{height:260px;position:relative;text-align:left;color:var(--white)}
.room .caption{position:absolute;left:0;right:0;bottom:0;padding:10px 14px;background:linear-gradient(0deg,rgba(0,0,0,.65),rgba(0,0,0,0))}
.room h3{font-size:18px;font-weight:600}
.room .row{display:flex;justify-content:space-between;font-size:11px}
.stars{color:var(--star);letter-spacing:1px}
.r1{background:linear-gradient(160deg,#5e6a55,#b8a58a)}
.r2{background:linear-gradient(160deg,#d9d3c9,#8b7f74)}
.r3{background:linear-gradient(160deg,#cfc7bd,#6b5e52)}
.r4{background:linear-gradient(160deg,#9a8a74,#e2dbd0)}
.r5{background:linear-gradient(160deg,#e3ddd2,#8e8274)}
.r6{background:linear-gradient(160deg,#4a4540,#b7aea2)}

/* video */
.video{height:460px;background:linear-gradient(180deg,#1d1410,#3a2012 45%,#24150d);position:relative;text-align:center;color:var(--white)}
.video h2{font-size:40px;font-weight:400;padding-top:160px}
.play{width:68px;height:68px;border-radius:50%;border:2px solid var(--white);margin:18px auto 0;display:flex;align-items:center;justify-content:center}

/* blog */
.blog{height:570px;padding-top:48px;text-align:center}
.blog-grid{display:grid;grid-template-columns:repeat(3,270px);gap:24px;justify-content:center}
.post{border:1px solid var(--line);text-align:left;height:394px}
.post .img{height:210px}
.post .body{padding:18px}
.post .date{color:var(--green);font-size:15px;font-weight:600;font-family:"Poppins",sans-serif}
.post h3{font-size:15px;font-weight:500;margin:2px 0 8px}
.post p{font-size:12px;color:var(--muted);line-height:1.5}
.b1{background:linear-gradient(180deg,#8fb0d0,#5b8040 55%,#6e5a44)}
.b2{background:linear-gradient(180deg,#7fa8cc,#4f7a36 50%,#9a9488)}
.b3{background:linear-gradient(180deg,#98b8d6,#67903f 55%,#3c5c28)}

/* testimonials */
.testimonials{height:452px;background:var(--green);text-align:center;color:var(--white);padding-top:48px}
.testimonials h2{font-size:36px;font-weight:600}
.avatar{width:110px;height:110px;border-radius:50%;border:4px solid var(--white);margin:18px auto 14px;background:linear-gradient(160deg,#c69a78,#6e4a34)}
.quote-row{display:flex;align-items:center;justify-content:center;gap:40px}
.arrow{width:30px;height:30px;border:1px solid var(--white);display:flex;align-items:center;justify-content:center}
.quote{width:660px;font-size:13px;position:relative}
.quote-mark{font-family:"Poppins",sans-serif;font-size:40px;font-weight:700;line-height:1;position:absolute}
.quote-mark.open{left:-24px;top:-8px}
.quote-mark.close{right:-20px;bottom:-30px}
.author{font-size:13px;font-weight:600;margin-top:18px}

/* footer */
.footer-nav{height:68px;background:var(--darker);display:flex;align-items:center;justify-content:center;gap:40px;font-family:"Poppins",sans-serif;font-size:12px;color:var(--white);text-transform:uppercase}
.footer{height:290px;background:var(--dark);color:var(--white)}
.footer .wrap{display:flex;justify-content:space-between;padding-top:36px}
.footer h4{font-size:16px;font-weight:600;text-transform:uppercase;margin-bottom:18px}
.form{width:330px;display:grid;grid-template-columns:1fr 1fr;gap:8px}
.form .in{background:var(--white);color:var(--muted);font-size:11px;height:30px;padding:6px 8px}
.form .wide{grid-column:span 2;height:52px}
.form .btn{grid-column:span 1;border-radius:2px;padding:6px 12px;font-size:11px;width:72px}
.contact{width:230px}
.contact .item{display:flex;gap:12px;margin-bottom:14px}
.contact .ico{width:32px;height:32px;border-radius:50%;background:var(--white);flex:none;display:flex;align-items:center;justify-content:center}
.contact b{display:block;font-size:13px;text-transform:uppercase}
.contact small{font-size:11px;color:#cfcfcf}
.footer-brand{padding-top:84px;text-align:center}
.footer-brand .brand{font-size:26px}
.footer-brand .socials{justify-content:center;margin-top:10px}
.copyright{height:62px;background:var(--darker);color:#cfcfcf;font-size:12px;display:flex;align-items:center;justify-content:center}
</style>
</head>
<body>

<div class="topbar">
  <div class="wrap">
    <div class="socials"><span></span><span></span><span></span><span></span></div>
    <div class="top-contact">
      <div>
        <svg width="14" height="10" viewBox="0 0 14 10"><rect x=".5" y=".5" width="13" height="9" fill="none" stroke="#fff"/><path d="M.5 .5 7 6 13.5 .5" fill="none" stroke="#fff"/></svg>
        Email: hello@hausweinberg.de
      </div>
      <div>
        <svg width="12" height="12" viewBox="0 0 24 24"><path fill="#fff" d="M6.6 10.8a15 15 0 0 0 6.6 6.6l2.2-2.2c.3-.3.7-.4 1-.2 1.1.4 2.3.6 3.6.6.6 0 1 .4 1 1V20c0 .6-.4 1-1 1A17 17 0 0 1 3 4c0-.6.4-1 1-1h3.5c.6 0 1 .4 1 1 0 1.3.2 2.5.6 3.6.1.3 0 .7-.2 1z"/></svg>
        Call Us: +49 (0) 6500 - 12 34 567
      </div>
    </div>
  </div>
</div>

<header class="nav">
  <div class="wrap">
    <div class="brand">Haus Weinberg</div>
    <nav class="menu">
      <a class="active" href="#">Home</a><a href="#">About</a><a href="#">Rooms</a><a href="#">Blog</a><a href="#">Gallery</a><a href="#">Contact Us</a>
      <a class="btn" href="#">Book Now</a>
    </nav>
  </div>
</header>

<section class="hero">
  <div class="hero-shade" role="img" aria-label="Garden terrace of the guest house with raised flower beds and paved path"></div>
  <div class="hero-copy">
    <h1>Haus Weinberg</h1>
    <p>Sed ut perspiciatis unde omnis iste natus error sit</p>
    <a class="btn" href="#">Learn More</a>
  </div>
  <form class="booking">
    <div class="field"><label>Arrival Date</label><div class="box">dd.mm.yyyy</div></div>
    <div class="field"><label>Departure Date</label><div class="box">dd.mm.yyyy</div></div>
    <div class="field"><label>Adults</label><div class="box">Adults <span>▾</span></div></div>
    <div class="field"><label>Children</label><div class="box">Children <span>▾</span></div></div>
    <a class="btn" href="#">Check Availability</a>
  </form>
</section>

<section class="welcome">
  <div class="wrap">
    <div class="welcome-text">
      <h4>Welcome to</h4>
      <h2>Haus Weinberg</h2>
      <p>Herzlich willkommen in unserem Haus an der Mosel. Wir laden Sie ein, in einem ehemaligen Kloster zur Ruhe zu kommen und den Blick auf die Weinberge und den Fluss zu genießen.</p>
      <p>Gastfreundschaft ist in unserer Familie eine lange Tradition, die wir gerne fortführen. Unser Haus ist denkmalgeschützt. Wir leben diese Geschichte und freuen uns auf Sie.</p>
      <a class="btn" href="#">Learn More</a>
    </div>
    <div class="welcome-photos">
      <div class="photo ph-night" role="img" aria-label="Historic house facade lit at night"></div>
      <div class="photo ph-valley" role="img" aria-label="Terrace overlooking the vineyard valley"></div>
      <div class="photo ph-candle" role="img" aria-label="Candle-lit outdoor dinner table"></div>
    </div>
  </div>
</section>

<section class="rooms">
  <h2 class="section-title">Our <span>Rooms</span></h2>
  <p class="section-sub">Each room is furnished in its own style, with quiet comfort and views of the river valley.</p>
  <div class="room-grid">
    <div class="room r1" role="img" aria-label="Guest room one with floral wallpaper"><div class="caption"><h3>Room 01</h3><div class="row"><span>Cosy double room with garden view</span><span class="stars">★★★★★</span></div></div></div>
    <div class="room r2" role="img" aria-label="Guest room two with bright bedding"><div class="caption"><h3>Room 02</h3><div class="row"><span>Bright room with modern details</span><span class="stars">★★★★★</span></div></div></div>
    <div class="room r3" role="img" aria-label="Guest room three with patterned wall"><div class="caption"><h3>Room 03</h3><div class="row"><span>Quiet room under old beams</span><span class="stars">★★★★★</span></div></div></div>
    <div class="room r4" role="img" aria-label="Guest room four with sitting area"><div class="caption"><h3>Room 04</h3><div class="row"><span>Spacious family room with sofa</span><span class="stars">★★★★★</span></div></div></div>
    <div class="room r5" role="img" aria-label="Guest room five with desk and lamp"><div class="caption"><h3>Room 05</h3><div class="row"><span>Calm room with reading corner</span><span class="stars">★★★★★</span></div></div></div>
    <div class="room r6" role="img" aria-label="Guest room six with dark headboard"><div class="caption"><h3>Room 06</h3><div class="row"><span>Elegant suite with river light</span><span class="stars">★★★★★</span></div></div></div>
  </div>
</section>

<section class="video" role="img" aria-label="Long dinner table set with candles and wine glasses">
  <h2>Haus Weinberg</h2>
  <div class="play"><svg width="24" height="26" viewBox="0 0 24 26"><path d="M4 2 22 13 4 24z" fill="#fff"/></svg></div>
</section>

<section class="blog">
  <h2 class="section-title">Latest <span>Blog</span></h2>
  <p class="section-sub">News from the house, the vineyards and the trails along the river.</p>
  <div class="blog-grid">
    <article class="post"><div class="img b1" role="img" aria-label="Garden with wooden fence and trees"></div><div class="body"><div class="date">27 Apr 2022</div><h3>Sed ut perspiciatis unde om</h3><p>Spring has arrived in our garden and the first guests are enjoying breakfast outside in the sun.</p></div></article>
    <article class="post"><div class="img b2" role="img" aria-label="Courtyard path lined with green plants"></div><div class="body"><div class="date">27 Apr 2022</div><h3>Sed ut perspiciatis unde om</h3><p>A short walk from the door leads to cycle routes, hiking trails and boat tours on the river.</p></div></article>
    <article class="post"><div class="img b3" role="img" aria-label="Lush garden with large palm plant"></div><div class="body"><div class="date">27 Apr 2022</div><h3>Sed ut perspiciatis unde om</h3><p>Our local winemakers open their cellars every weekend for tastings and relaxed evenings.</p></div></article>
  </div>
</section>

<section class="testimonials">
  <h2>Testimonials</h2>
  <div class="avatar" role="img" aria-label="Guest portrait"></div>
  <div class="quote-row">
    <div class="arrow"><svg width="8" height="12" viewBox="0 0 8 12"><path d="M7 1 2 6l5 5" fill="none" stroke="#fff" stroke-width="2"/></svg></div>
    <div class="quote">
      <span class="quote-mark open">“</span>
      We came for a weekend and stayed a whole week. The rooms are beautiful and every one is different, breakfast was fresh and generous, and the family made us feel at home from the first minute. The view over the vineyards in the evening is simply wonderful. We will certainly come back next summer with the children.
      <span class="quote-mark close">”</span>
      <div class="author">- Jana Keller</div>
    </div>
    <div class="arrow"><svg width="8" height="12" viewBox="0 0 8 12"><path d="M1 1l5 5-5 5" fill="none" stroke="#fff" stroke-width="2"/></svg></div>
  </div>
</section>

<nav class="footer-nav"><span>Home</span><span>About</span><span>Rooms</span><span>Blog</span><span>Gallery</span><span>Contact Us</span></nav>

<footer class="footer">
  <div class="wrap">
    <div>
      <h4>Get In Touch</h4>
      <div class="form">
        <div class="in">First Name</div><div class="in">Last Name</div>
        <div class="in">Email</div><div class="in">Phone</div>
        <div class="in wide">Message</div>
        <div class="btn">Submit</div>
      </div>
    </div>
    <div class="contact">
      <h4>Contact Info</h4>
      <div class="item"><div class="ico"><svg width="14" height="16" viewBox="0 0 24 28"><path d="M12 0a10 10 0 0 0-10 10c0 7 10 18 10 18s10-11 10-18A10 10 0 0 0 12 0zm0 14a4 4 0 1 1 0-8 4 4 0 0 1 0 8z" fill="#6a9a2c"/></svg></div><div><b>Address</b><small>Weinbergstraße 12, 54000 Moseltal</small></div></div>
      <div class="item"><div class="ico"><svg width="14" height="14" viewBox="0 0 24 24"><path fill="#6a9a2c" d="M6.6 10.8a15 15 0 0 0 6.6 6.6l2.2-2.2c.3-.3.7-.4 1-.2 1.1.4 2.3.6 3.6.6.6 0 1 .4 1 1V20c0 .6-.4 1-1 1A17 17 0 0 1 3 4c0-.6.4-1 1-1h3.5c.6 0 1 .4 1 1 0 1.3.2 2.5.6 3.6.1.3 0 .7-.2 1z"/></svg></div><div><b>Phone</b><small>+49 (0) 6500 - 12 34 567</small></div></div>
      <div class="item"><div class="ico"><svg width="14" height="10" viewBox="0 0 14 10"><rect x=".5" y=".5" width="13" height="9" fill="none" stroke="#6a9a2c"/><path d="M.5 .5 7 6 13.5 .5" fill="none" stroke="#6a9a2c"/></svg></div><div><b>Email</b><small>hello@hausweinberg.de</small></div></div>
    </div>
    <div class="footer-brand">
      <div class="brand">Haus Weinberg</div>
      <div class="socials"><span></span><span></span><span></span><span></span></div>
    </div>
  </div>
</footer>

<div class="copyright">© Copyright 2022 Haus Weinberg. All Rights Reserved</div>

</body>
</html>
```